Makeup Artist

Hi I am makeup artist I attached the business card that I found on the net love the design.
I would love something like this simple but looking expensive.
I want double side business card. Front my full name. my phone number, email address and facebook and my next appointment is... on the other side.
Thank you :)

Hello I change my Facebook account - Makeup by Kolina, if you could please update your designs , thank you

Target Market(s)

high end clientele

Industry/Entity Type

Business

Colors
ec2027
ffc214
33b7a4
6b449b
e34197
9bcb3c
f37122
a64599

Requirements
Must have
• bright colours
Should not have
• brushes or whole lipsticks

```html
<!DOCTYPE html>
<html lang="en">
<head>
<meta charset="utf-8">
<title>Kolina Dravenko – Make Up Artist business card</title>
<link href="https://fonts.googleapis.com/css2?family=Dosis:wght@300;400;500&display=swap" rel="stylesheet">
<style>
  :root {
    --backdrop: #d9d6d2;
    --card: #1c1a19;
    --card-edge: #262322;
    --gold: #c9a24a;
    --gold-light: #e4c476;
    --ink: #e9e6e2;
    --ink-soft: #a9a4a0;
    --red: #ec2027;
    --yellow: #ffc214;
    --teal: #33b7a4;
    --purple: #6b449b;
    --pink: #e34197;
    --lime: #9bcb3c;
    --orange: #f37122;
    --violet: #a64599;
  }
  * { box-sizing: border-box; margin: 0; padding: 0; }
  html, body { width: 1200px; height: 873px; overflow: hidden; }
  body {
    background: var(--backdrop);
    font-family: "Dosis", sans-serif;
    display: flex;
    align-items: center;
    justify-content: center;
    gap: 40px;
  }
  .card {
    position: relative;
    width: 560px;
    height: 320px;
    background: radial-gradient(ellipse at 30% 40%, var(--card-edge), var(--card) 70%);
    border-radius: 6px;
    box-shadow: 0 10px 30px rgba(0,0,0,.25);
    overflow: hidden;
    color: var(--ink);
  }

  /* Back side: contact details */
  .card-back .contact {
    position: absolute;
    left: 64px;
    top: 58px;
    font-weight: 300;
  }
  .phone { font-size: 40px; letter-spacing: 3px; line-height: 1.1; }
  .email { font-size: 26px; letter-spacing: 1px; margin-top: 10px; }
  .social {
    display: flex; align-items: center; gap: 12px;
    font-size: 26px; letter-spacing: 1px; margin-top: 10px;
  }
  .social-mark { width: 18px; height: 18px; background: var(--gold); border-radius: 2px; }
  .appointment {
    position: absolute;
    left: 64px; right: 64px; bottom: 40px;
    display: flex; align-items: flex-end; gap: 10px;
    color: var(--gold);
    font-size: 19px; font-weight: 400; letter-spacing: 1px;
  }
  .appointment-line { flex: 1; border-bottom: 1px dotted var(--gold); margin-bottom: 5px; }
  .time-line {
    position: absolute; left: 64px; width: 50px; bottom: 86px;
    border-bottom: 1px solid var(--ink-soft);
  }

  /* Front side: name and palette */
  .palette {
    position: absolute;
    left: 34px; top: 44px;
    display: grid;
    grid-template-columns: repeat(2, 78px);
    column-gap: 14px;
    row-gap: 14px;
  }
  .pan {
    width: 78px; height: 46px;
    border-radius: 6px;
    box-shadow: inset 0 2px 4px rgba(255,255,255,.45), inset 0 -3px 6px rgba(0,0,0,.35), 0 0 10px var(--glow);
  }
  .pan:nth-child(even) { transform: translateY(-30px); }
  .pan-orange { background: var(--orange); --glow: rgba(243,113,34,.5); }
  .pan-purple { background: var(--purple); --glow: rgba(107,68,155,.5); }
  .pan-yellow { background: var(--yellow); --glow: rgba(255,194,20,.5); }
  .pan-violet { background: var(--violet); --glow: rgba(166,69,153,.5); }
  .pan-lime { background: var(--lime); --glow: rgba(155,203,60,.5); }
  .pan-pink { background: var(--pink); --glow: rgba(227,65,151,.5); }
  .pan-teal { background: var(--teal); --glow: rgba(51,183,164,.5); }
  .pan-red { background: var(--red); --glow: rgba(236,32,39,.5); }

  .flourish {
    position: absolute;
    left: 250px; top: 60px;
    width: 90px; height: 56px;
    border-radius: 28px;
    background: radial-gradient(ellipse, rgba(228,196,118,.55), rgba(201,162,74,0) 70%);
  }
  .brand {
    position: absolute;
    left: 250px; top: 130px;
  }
  .brand-name {
    color: var(--gold-light);
    font-size: 40px; font-weight: 500; letter-spacing: 1px;
  }
  .brand-role {
    color: var(--ink-soft);
    font-size: 20px; font-weight: 300; letter-spacing: 2px;
    margin-top: 6px; text-align: right;
  }
</style>
</head>
<body>
  <section class="card card-back" aria-label="Business card, back">
    <div class="contact">
      <p class="phone">0491 570 156</p>
      <p class="email">hello@kolinadravenko.com</p>
      <p class="social"><span class="social-mark"></span>Makeup by Kolina</p>
    </div>
    <div class="time-line"></div>
    <p class="appointment">My next appointment is:<span class="appointment-line"></span></p>
  </section>

  <section class="card card-front" aria-label="Business card, front">
    <div class="palette">
      <div class="pan pan-orange"></div>
      <div class="pan pan-purple"></div>
      <div class="pan pan-yellow"></div>
      <div class="pan pan-violet"></div>
      <div class="pan pan-lime"></div>
      <div class="pan pan-pink"></div>
      <div class="pan pan-teal"></div>
      <div class="pan pan-red"></div>
    </div>
    <div class="flourish" role="img" aria-label="Gold decorative swirl ornament"></div>
    <div class="brand">
      <h1 class="brand-name">Kolina Dravenko</h1>
      <p class="brand-role">Make Up Artist</p>
    </div>
  </section>
</body>
</html>
```